Software Engineering Company need eye catching banner for and Engineering conventions

We need an eye-catching banner designed. The size of the banner will be 34" W x 81" H. We develop routing software installed in bus systems and use GPS real-time tracking to always know where they are. We would like the banner to be dominated by the colors in our logo, 2 different blues, dark gray and of course white and black if needed. We are hoping for something that will pop out and look awesome. If you want to use our entire name or just our logo is completely up to you.

Target Market(s)

Young Engineers looking for new and cutting edge job opportunities

Industry/Entity Type

Computer Software

Colors
1f68ae
3779b6
ffffff

Requirements
Should not have
• the colors in our logo

```html
<!DOCTYPE html>
<html lang="en">
<head>
<meta charset="utf-8">
<title>Velora Technologies LLC Banner</title>
<link href="https://fonts.googleapis.com/css2?family=Montserrat:wght@400;500;600;700&display=swap" rel="stylesheet">
<style>
  :root {
    --sky: #27a0dc;
    --navy: #1060ae;
    --brand-blue: #1f68ae;
    --ink: #151515;
    --paper: #ffffff;
    --gray-text: #5e6166;
    --photo-top: #4f9fd0;
    --photo-mid: #9cc4e2;
    --photo-low: #cfe0ef;
  }
  * { margin: 0; padding: 0; box-sizing: border-box; }
  html, body { width: 1200px; height: 2859px; overflow: hidden; background: var(--paper); }
  body { font-family: "Montserrat", Arial, sans-serif; position: relative; }

  .hero {
    position: absolute; left: 0; top: 0; width: 1200px; height: 1787px;
    background: linear-gradient(160deg, var(--photo-top) 0%, #74b2dc 30%, var(--photo-mid) 60%, var(--photo-low) 100%);
  }
  .hero-headline {
    position: absolute; left: 145px; top: 318px;
    color: var(--paper); font-size: 78px; font-weight: 500; line-height: 156px;
    letter-spacing: 2px;
  }
  .hero-headline strong { font-weight: 700; }

  .brand {
    position: absolute; left: 0; top: 1560px; width: 1200px;
    display: flex; justify-content: center; align-items: center; gap: 28px;
  }
  .brand-square { width: 92px; height: 92px; background: var(--brand-blue); }
  .brand-name {
    color: var(--brand-blue); font-size: 64px; font-weight: 700; letter-spacing: 2px;
    line-height: 1.1;
  }

  .band { position: absolute; left: 0; width: 1200px; display: flex; align-items: center; justify-content: center; color: var(--paper); }
  .web-band { top: 1805px; height: 199px; background: var(--ink); font-size: 78px; font-weight: 500; letter-spacing: 2px; }
  .phone-band { top: 2015px; height: 225px; background: var(--sky); font-size: 92px; font-weight: 500; letter-spacing: 1px; }

  .intro { position: absolute; left: 0; top: 2240px; width: 1200px; height: 360px; text-align: center; }
  .intro-title { margin-top: 92px; color: var(--sky); font-size: 45px; font-weight: 700; letter-spacing: 1px; }
  .intro-text { margin-top: 20px; color: var(--gray-text); font-size: 33px; font-weight: 500; line-height: 55px; letter-spacing: 1.5px; }

  .cta-band { position: absolute; left: 0; top: 2600px; width: 1200px; height: 259px; background: var(--navy); }
  .cta-button {
    position: absolute; left: 209px; top: 63px; width: 774px; height: 130px;
    background: var(--sky); border-radius: 6px;
    display: flex; align-items: center; justify-content: center;
    color: var(--paper); font-size: 46px; font-weight: 700; letter-spacing: 2px;
  }
</style>
</head>
<body>
  <section class="hero" role="img" aria-label="Photo of hands typing on a keyboard in front of a monitor showing a street map with route pins, tinted blue">
    <h1 class="hero-headline">Lorem ipsum dolor sit<br>amet, <strong>consectetur</strong><br><strong>adipiscing elit</strong></h1>
    <div class="brand">
      <span class="brand-square"></span>
      <span class="brand-name">VELORA TECHNOLOGIES</span>
    </div>
  </section>

  <div class="band web-band">www.veloratech.com</div>
  <div class="band phone-band">152-555-0147</div>

  <section class="intro">
    <h2 class="intro-title">LOREM IPSUM DOLOR SIT AMET</h2>
    <p class="intro-text">Lorem ipsum dolor sit amet, consectetur adipiscing<br>elit. Curabitur iaculis tortor id varius venenatis.</p>
  </section>

  <section class="cta-band">
    <div class="cta-button">GET STARTED</div>
  </section>
</body>
</html>
```